Tallowcrest Rise A4 Potrait foldout brochure

We need a brochure design for this residential land development. I have attached the a style that we like to base our design on. Full colour required. will provide files required for design also. PLEASE DO NOT COPY THIS DESIGN. Come up with a new style that gives you this feeling. Please note the plan needs to be positioned landscape on the inside 2 A4 Pages.

Industry/Entity Type

Residential

Other font styles liked:
• Try with Century Gothich

Requirements
Must have
• use same colours as supplied in Tallowcrest rise brochure.
Nice to have
• nice modern simple background graphics

```html
<!DOCTYPE html>
<html lang="en">
<head>
<meta charset="utf-8">
<title>Tallowcrest Rise – Brochure Covers</title>
<link rel="stylesheet" href="https://fonts.googleapis.com/css2?family=Questrial&display=swap">
<style>
  :root {
    --sheet: #ffffff;
    --teal: #00a79a;
    --teal-deep: #0a84ae;
    --paper: #f2f2f2;
    --frame: #1aa39a;
    --bloom-light: #e6e6e6;
    --bloom-light-edge: #cfd6d6;
    --bloom-teal: #17a79c;
    --bloom-blue: #1a78b4;
    --ink-white: #ffffff;
    --ink-forest: #1f4a2c;
  }
  * { margin: 0; padding: 0; box-sizing: border-box; }
  html, body {
    width: 1200px; height: 855px; overflow: hidden;
    background: var(--sheet);
    font-family: "Questrial", "Century Gothic", sans-serif;
  }
  .spread { position: relative; width: 1200px; height: 855px; }
  .page {
    position: absolute; top: 12px; width: 583px; height: 831px; overflow: hidden;
  }
  .page--front {
    left: 12px;
    background: linear-gradient(180deg, var(--teal) 0%, var(--teal) 45%, var(--teal-deep) 100%);
  }
  .page--inner {
    left: 606px;
    background: var(--paper);
    border: 1px solid var(--frame);
  }
  .bloom { position: absolute; border-radius: 50%; }
  .bloom--front-top {
    left: 458px; top: 2px; width: 140px; height: 250px; border-radius: 50% 0 0 50% / 50% 0 0 50%;
    background: radial-gradient(circle at 70% 50%, var(--bloom-light) 0%, var(--bloom-light-edge) 100%);
    opacity: .85;
  }
  .bloom--front-side {
    left: -250px; top: 340px; width: 495px; height: 495px;
    background: radial-gradient(circle, var(--bloom-light) 0%, var(--bloom-light-edge) 100%);
    opacity: .85;
  }
  .bloom--inner-top {
    left: -70px; top: 4px; width: 192px; height: 248px; border-radius: 0 50% 50% 0 / 0 50% 50% 0;
    background: radial-gradient(circle at 30% 50%, var(--bloom-teal) 0%, var(--bloom-blue) 100%);
  }
  .bloom--inner-side {
    left: 336px; top: 338px; width: 495px; height: 495px;
    background: linear-gradient(200deg, var(--bloom-blue) 0%, var(--bloom-teal) 55%, var(--bloom-teal) 100%);
  }
  .wordmark { position: absolute; white-space: nowrap; }
  .wordmark__name { display: block; line-height: 1; }
  .wordmark__place { display: block; text-align: right; line-height: 1; }
  .wordmark--front { left: 80px; top: 240px; color: var(--ink-white); }
  .wordmark--front .wordmark__name { font-size: 47px; }
  .wordmark--front .wordmark__place { font-size: 10px; margin-top: 6px; }
  .wordmark--inner { left: 33px; top: 747px; color: var(--ink-forest); }
  .wordmark--inner .wordmark__name { font-size: 41px; }
  .wordmark--inner .wordmark__place { font-size: 9px; margin-top: 4px; }
</style>
</head>
<body>
<main class="spread">
  <section class="page page--front">
    <div class="bloom bloom--front-top" role="img" aria-label="Light floral vine pattern arranged in a circle"></div>
    <div class="bloom bloom--front-side" role="img" aria-label="Large light floral vine pattern arranged in a circle"></div>
    <h1 class="wordmark wordmark--front">
      <span class="wordmark__name">Tallowcrest Rise</span>
      <span class="wordmark__place">Tallowcrest Vale</span>
    </h1>
  </section>
  <section class="page page--inner">
    <div class="bloom bloom--inner-top" role="img" aria-label="Teal and blue floral vine pattern arranged in a circle"></div>
    <div class="bloom bloom--inner-side" role="img" aria-label="Large teal and blue floral vine pattern arranged in a circle"></div>
    <h2 class="wordmark wordmark--inner">
      <span class="wordmark__name">Tallowcrest Rise</span>
      <span class="wordmark__place">Tallowcrest Vale</span>
    </h2>
  </section>
</main>
</body>
</html>
```